Business Card Design

Divorce
Collaborative Family Law
Family Dispute Resolution
Family Law Property & Children

Target Market(s)

Australia

Industry/Entity Type

Business

Contact Information for Business Card

Delia Frampton
M App Law (Family Law) LLB (Hons) BA (Hons) Ass Dip Ag (HH)
Family Dispute Resolution Provider
Frampton Family Law
PO Box 4372 Wendlebury 3914
Phone 03 57218300 Fax 03 57218399 Email framptonfamilylaw@quillmail.example

Colors
f04a51

Requirements
Should not have
• Any reference to
United States or US terminology
the word Company

```html
<!DOCTYPE html>
<html lang="en">
<head>
<meta charset="utf-8">
<title>Frampton Family Law – Business Card</title>
<link rel="stylesheet" href="https://fonts.googleapis.com/css2?family=Playfair+Display:wght@600;700&family=Open+Sans:ital,wght@1,700&family=Arimo:wght@400;700&display=swap">
<style>
  :root {
    --red-deep: #5a0a0e;
    --red-mid: #8e1519;
    --red-bright: #b5262b;
    --red-glow: #f04a51;
    --white: #ffffff;
    --text-soft: #f6eaea;
  }
  html, body {
    margin: 0;
    padding: 0;
    width: 1200px;
    height: 744px;
    overflow: hidden;
    background: #ffffff;
  }
  .card {
    position: relative;
    width: 1192px;
    height: 736px;
    margin: 4px;
    border-radius: 6px;
    overflow: hidden;
    background:
      radial-gradient(ellipse 55% 60% at 42% 38%, rgba(240, 74, 81, 0.55), rgba(240, 74, 81, 0) 70%),
      linear-gradient(160deg, var(--red-mid) 0%, var(--red-bright) 40%, var(--red-mid) 70%, var(--red-deep) 100%);
    box-shadow: 0 2px 6px rgba(0, 0, 0, 0.4);
  }
  .backdrop-photo {
    position: absolute;
    left: 0;
    top: 60px;
    width: 700px;
    height: 676px;
    background:
      radial-gradient(ellipse 40% 30% at 45% 82%, rgba(40, 4, 6, 0.45), rgba(40, 4, 6, 0) 70%),
      radial-gradient(ellipse 45% 35% at 50% 30%, rgba(255, 170, 170, 0.18), rgba(255, 170, 170, 0) 70%);
  }
  .divider {
    position: absolute;
    left: 30px;
    width: 1140px;
    height: 3px;
    background: linear-gradient(90deg, rgba(255,255,255,0) 0%, var(--white) 8%, var(--white) 92%, rgba(255,255,255,0) 100%);
  }
  .divider--upper { top: 284px; }
  .divider--lower { top: 493px; }
  .firm-name, .person-name {
    position: absolute;
    left: 0;
    top: 0;
  }
  .firm-name text, .person-name text {
    font-family: "Playfair Display", "Bodoni Moda", serif;
    fill: var(--white);
  }
  .credentials {
    position: absolute;
    left: 706px;
    top: 314px;
    margin: 0;
    padding: 0;
    list-style: none;
    font-family: "Open Sans", Arial, sans-serif;
    font-style: italic;
    font-weight: 700;
    font-size: 25px;
    color: var(--white);
  }
  .credentials li {
    position: relative;
    padding-left: 30px;
    line-height: 41px;
  }
  .credentials li::before {
    content: "";
    position: absolute;
    left: 0;
    top: 16px;
    width: 10px;
    height: 10px;
    border-radius: 50%;
    background: var(--white);
  }
  .contact {
    position: absolute;
    left: 643px;
    top: 527px;
    font-family: "Arimo", Arial, sans-serif;
    font-size: 27px;
    color: var(--text-soft);
    line-height: 39.5px;
  }
  .contact__address { padding-left: 100px; }
  .contact__row { display: flex; }
  .contact__label { width: 41px; }
  .contact__value--strong { font-weight: 700; color: var(--white); }
</style>
</head>
<body>
<div class="card">
  <div class="backdrop-photo" role="img" aria-label="Faint photograph of a judge's gavel and scales of justice"></div>

  <svg class="firm-name" width="1192" height="260" viewBox="0 0 1192 260">
    <text x="62" y="182" font-size="150" font-weight="700" textLength="1066" lengthAdjust="spacingAndGlyphs">Frampton Family Law</text>
  </svg>

  <div class="divider divider--upper"></div>

  <svg class="person-name" width="700" height="480" viewBox="0 0 700 480">
    <text x="72" y="422" font-size="86" font-weight="600" textLength="600" lengthAdjust="spacingAndGlyphs">Delia Frampton</text>
  </svg>

  <ul class="credentials">
    <li>M App Law (Family Law)</li>
    <li>LLB (Hons) BA (Hons)</li>
    <li>Ass Dip Ag (HH)</li>
    <li>Family Dispute Resolution Provider</li>
  </ul>

  <div class="divider divider--lower"></div>

  <div class="contact">
    <div class="contact__address">PO Box 4372 Wendlebury 3914</div>
    <div class="contact__row"><span class="contact__label">p:</span><span class="contact__value--strong">03 57218300</span></div>
    <div class="contact__row"><span class="contact__label">f:</span><span class="contact__value--strong">03 57218399</span></div>
    <div class="contact__row"><span class="contact__label">e:</span><span>framptonfamilylaw@quillmail.example</span></div>
  </div>
</div>
</body>
</html>
```